Flyer für Beratung, Planung und Montage von Photovoltaikanlagen, Wallboxen usw.
Der Ablauf war optimal. Auf Änderungswünsche wurde umgehend eingegangen. Die Bearbeitung erfolgt sehr zeitnah. Wir sind sehr zufrieden und können TOLVERIKO nur empfehlen.
Zielgruppe
Individuelle Beratung, Planung und Montage von Photovoltaikanlagen, Wallboxen, Balkonkraftwerke, PowerToHeat, Stromspeicher etc., (Neuanlagen & Bestandsanlagen), Privat- & Firmenkunden
Aufgabenstellung
Qualitativ hochwertige Markenprodukte, Seriös, Modern, Regionaler Anbieter, Flyer für gezielte regionale Verteilung (Briefkasten)

```html
<!DOCTYPE html>
<html lang="de">
<head>
<meta charset="utf-8">
<title>Nordwerk Energie – Flyer</title>
<link href="https://fonts.googleapis.com/css2?family=Poppins:ital,wght@0,400;0,500;0,600;0,700;0,800;1,700;1,800&display=swap" rel="stylesheet">
<style>
:root{
  --lime:#c9d92c;
  --slate:#4c5653;
  --ink:#111;
  --paper:#fff;
  --sky1:#2a70c9;
  --sky2:#74b0e8;
}
*{margin:0;padding:0;box-sizing:border-box}
html,body{width:1200px;height:3144px;overflow:hidden;background:var(--paper);font-family:'Poppins',sans-serif;color:var(--ink)}
.spread{position:absolute;left:81px;width:1032px;height:730px;display:flex;box-shadow:0 2px 8px rgba(0,0,0,.35)}
.page{position:relative;width:516px;height:100%;overflow:hidden;background:var(--paper)}
.photo{position:absolute}
.brand{display:flex;align-items:center;justify-content:center;gap:10px;font-weight:600;color:var(--lime);letter-spacing:3px}
.brand .mark{width:14px;height:14px;background:var(--slate)}
p{font-size:12px;line-height:1.6}
h2{font-weight:800;font-size:24px;line-height:1.15}
/* spread 1 */
.s1{top:84px}
.cover .brand{position:absolute;top:170px;left:0;right:0;font-size:24px}
.cover .claim{position:absolute;top:208px;left:0;right:0;text-align:center;font-size:26px;line-height:1.3}
.cover .claim b{font-weight:800}
.about{background:linear-gradient(180deg,var(--sky1) 0%,var(--sky2) 60%,#2c3a55 100%)}
.about h2{position:absolute;top:60px;left:23px;color:#fff;font-size:28px}
.about p{position:absolute;top:110px;left:35px;right:38px;color:#fff;text-align:justify;font-size:13.5px;line-height:1.5}
/* spread 2 */
.s2{top:840px}
.services h2{position:absolute;top:33px;left:31px;font-size:25px}
.services .rule{position:absolute;top:49px;left:292px;right:0;height:3px;background:var(--lime)}
.services .dark{position:absolute;top:403px;left:0;right:0;bottom:0;background:var(--slate)}
.row{position:absolute;left:0;right:0}
.row .num{position:absolute;left:33px;font-weight:800;font-size:82px;color:var(--lime);line-height:1}
.row .tile{position:absolute;left:161px;right:0;top:0;bottom:0}
.row .tile span{position:absolute;left:14px;bottom:6px;color:#fff;font-weight:800;font-size:23px;line-height:1.15;text-shadow:0 1px 3px rgba(0,0,0,.6)}
.pv .rule-v{position:absolute;left:476px;top:90px;width:3px;height:160px;background:var(--lime)}
.pv .rule-h{position:absolute;left:265px;top:240px;width:230px;height:3px;background:var(--lime)}
.pv h2{position:absolute;top:252px;left:35px;font-size:23px}
.pv .body{position:absolute;top:292px;left:37px;right:20px}
.pv .body p{font-size:11.5px;margin-bottom:12px}
.pv ul{list-style:none}
.pv li{display:flex;align-items:center;gap:14px;font-weight:600;font-size:11.5px;margin-bottom:12px}
.pv li svg{flex:none}
/* spread 3 */
.s3{top:1596px}
.storage .head{position:absolute;top:0;left:0;width:250px;height:156px;background:var(--slate)}
.storage .head .rule{position:absolute;top:34px;left:28px;width:250px;height:3px;background:var(--lime)}
.storage .head h2{position:absolute;top:55px;left:28px;color:#fff;font-size:26px}
.storage .head p{position:absolute;top:95px;left:28px;color:#fff;font-size:11.5px;line-height:1.3}
.storage .intro{position:absolute;top:172px;left:28px;width:218px;font-size:12px;text-align:justify}
.storage .dark{position:absolute;top:527px;left:0;right:0;bottom:0;background:var(--slate);padding:30px 28px 0}
.storage .dark p{color:#fff;font-size:11.5px;margin-bottom:14px}
.charge h2{position:absolute;top:34px;left:35px;font-size:22px}
.charge .intro{position:absolute;top:100px;left:35px;right:18px;font-size:11.5px}
.charge .quote{position:absolute;top:455px;left:0;right:0;bottom:0;background:linear-gradient(90deg,#9a9d9c,#c8c9c8 40%,#7e8281)}
.charge .quote-text{position:absolute;top:570px;left:210px;right:38px;color:#fff;font-weight:800;font-style:italic;font-size:17px;line-height:1.3}
.charge .qmark{position:absolute;top:498px;left:213px}
.charge .qline{position:absolute;top:669px;left:290px;right:0;height:3px;background:var(--lime)}
/* spread 4 */
.s4{top:2352px}
.maint .head{position:absolute;top:0;left:0;right:0;height:154px;background:var(--slate)}
.maint .head h2{position:absolute;top:55px;left:0;right:0;text-align:center;color:#fff;font-size:26px}
.maint .head .rule{position:absolute;top:108px;left:132px;width:252px;height:3px;background:var(--lime)}
.maint p{position:absolute;top:188px;left:30px;right:30px;text-align:center;font-size:12px}
.back .band-top{position:absolute;top:0;left:0;right:0;height:29px;background:var(--lime)}
.back .band-bot{position:absolute;bottom:0;left:0;right:0;height:30px;background:var(--slate)}
.back .brand{position:absolute;top:390px;left:0;right:0;font-size:30px}
.back .brand .mark{width:20px;height:20px}
.back p{position:absolute;top:495px;left:60px;right:60px;text-align:center;font-size:14px;line-height:1.4}
</style>
</head>
<body>

<section class="spread s1">
  <div class="page cover">
    <div class="brand"><span class="mark"></span>NORDWERK ENERGIE</div>
    <div class="claim"><b>Ihr Regionaler Anbieter</b><br>Für Erneuerbare Energien</div>
    <div class="photo" role="img" aria-label="Solarpark unter blauem Himmel" style="left:15px;top:304px;width:485px;height:425px;background:linear-gradient(180deg,#2f72c6 0%,#8dbbe8 55%,#27364f 78%,#53622f 100%)"></div>
  </div>
  <div class="page about" role="img" aria-label="Windrad über Solarmodulen vor blauem Himmel">
    <h2>Uber Uns</h2>
    <p>Wir sind Ihre regionalen Experten für maßgeschneiderte Photovoltaik- und Stromspeicherlösungen. Egal, ob Sie Privat- oder Gewerbekunde sind. Wir bieten passgenaue Lösungen und 360° Service für Ihre individuellen Bedürfnisse – und das sowohl für Neu- als auch Bestandsanlagen. Von der detaillierten Planung bis zur professionellen Installation und darüber hinaus.</p>
  </div>
</section>

<section class="spread s2">
  <div class="page services">
    <h2>Unsere Leistungen</h2>
    <div class="rule"></div>
    <div class="dark"></div>
    <div class="row" style="top:88px;height:134px">
      <div class="num" style="top:36px">01</div>
      <div class="tile" role="img" aria-label="Wohnhäuser mit Solardach in der Abenddämmerung" style="background:linear-gradient(180deg,#6f8aa6,#3d4a45 70%,#2a3326)"><span>Photovoltaikanlage</span></div>
    </div>
    <div class="row" style="top:255px;height:118px">
      <div class="num" style="top:22px">02</div>
      <div class="tile" role="img" aria-label="Verschiedene Stromspeicher-Geräte" style="background:linear-gradient(90deg,#2c2626 0%,#2c2626 30%,#f2f2f2 34%,#e4e4e4 60%,#fff 100%)"><span>Stromspeicher</span></div>
    </div>
    <div class="row" style="top:403px;height:136px">
      <div class="num" style="top:36px">03</div>
      <div class="tile" role="img" aria-label="Elektroauto an Ladestation vor einem Haus" style="background:linear-gradient(90deg,#6b7060,#8e8670 50%,#e8ebe8)"><span>Ladeinfrastruktur<br>und Elektromobilität</span></div>
    </div>
    <div class="row" style="top:561px;height:136px">
      <div class="num" style="top:36px">04</div>
      <div class="tile" role="img" aria-label="Würfel mit Zufriedenheitssymbolen auf Solarmodul" style="background:linear-gradient(90deg,#9aa3ab,#dcdcd8 60%,#f0ede8)"><span>Wartung, Service<br>And Monitoring</span></div>
    </div>
  </div>
  <div class="page pv">
    <div class="photo" role="img" aria-label="Modernes Haus mit Solardach bei Sonnenuntergang" style="left:23px;top:25px;width:472px;height:204px;background:linear-gradient(180deg,#b9c8d6,#47505a 45%,#a26e3f 80%,#5d6b3a)"></div>
    <div class="rule-v"></div>
    <div class="rule-h"></div>
    <h2>Photovoltaikanlage</h2>
    <div class="body">
      <p>Egal ob Eigenheim mit oder ohne Bestandsanlage, Gewerbeimmobilie oder Freifläche. Wir finden gemeinsam die passende Lösung für Sie!</p>
      <p><b>Besichtigung:</b> Um Ihnen ein adäquates Angebot unterbreiten zu können, kommen wir persönlich zu Ihnen, um festzustellen ob Ihr Haus oder Gebäude für eine Photovoltaikanlage geeignet ist und mit welchem Aufwand Sie rechnen müssen.</p>
      <p><b>zum Beispiel:</b></p>
      <ul>
        <li><svg width="16" height="16" viewBox="0 0 16 16"><rect x="1" y="1" width="14" height="14" fill="none" stroke="#c9d92c" stroke-width="2"/><path d="M4 8l3 3 5-6" fill="none" stroke="#c9d92c" stroke-width="2"/></svg>Fläche und Dachneigung</li>
        <li><svg width="16" height="16" viewBox="0 0 16 16"><rect x="1" y="1" width="14" height="14" fill="none" stroke="#c9d92c" stroke-width="2"/><path d="M4 8l3 3 5-6" fill="none" stroke="#c9d92c" stroke-width="2"/></svg>Unterkonstruktion und Dacheindeckung</li>
        <li><svg width="16" height="16" viewBox="0 0 16 16"><rect x="1" y="1" width="14" height="14" fill="none" stroke="#c9d92c" stroke-width="2"/><path d="M4 8l3 3 5-6" fill="none" stroke="#c9d92c" stroke-width="2"/></svg>Ausrichtung und Beschattung</li>
        <li><svg width="16" height="16" viewBox="0 0 16 16"><rect x="1" y="1" width="14" height="14" fill="none" stroke="#c9d92c" stroke-width="2"/><path d="M4 8l3 3 5-6" fill="none" stroke="#c9d92c" stroke-width="2"/></svg>Hindernisse, Nebengebäude und geografischer Standort</li>
      </ul>
    </div>
    <div class="photo" role="img" aria-label="Gewerbehalle mit Solardach bei Sonnenuntergang" style="left:0;top:612px;width:516px;height:118px;background:linear-gradient(180deg,#f1b06d,#6f6a6b 45%,#2f3640)"></div>
  </div>
</section>

<section class="spread s3">
  <div class="page storage">
    <div class="head">
      <div class="rule"></div>
      <h2>Stromspeicher</h2>
      <p>Privat- oder Gewerbespeicher<br>für alle Bedürfnisse</p>
    </div>
    <p class="intro">Privat- oder Gewerbespeicher, DC oder AC gekoppelt, Notstrom- oder Ersatzstromfähigkeit, Lastspitzenkappung (Peak Shaving)</p>
    <div class="photo" role="img" aria-label="Hoher schwarzer Stromspeicher-Schrank" style="left:355px;top:40px;width:85px;height:225px;background:linear-gradient(90deg,#111,#3a3a3a 50%,#151515)"></div>
    <div class="photo" role="img" aria-label="Schwarzer Wand-Stromspeicher" style="left:68px;top:313px;width:130px;height:150px;background:linear-gradient(135deg,#3a3a3a,#0d0d0d)"></div>
    <div class="photo" role="img" aria-label="Modularer Stromspeicher mit Erweiterungsschränken" style="left:282px;top:375px;width:188px;height:145px;background:linear-gradient(90deg,#261818,#2d2424 20%,#d8d8d8 25%,#cfcfcf 35%,#181414 38%)"></div>
    <div class="dark">
      <p><b>Erweiterung:</b> Sie haben bereits eine PV – Anlage und möchten diese mit einem Energiespeicher erweitern?</p>
      <p><b>Nachrüstung:</b> Ihr bisheriger Speicher ist zu klein, wir prüfen die Erweiterbarkeit Ihres Systems – und geben eine Empfehlung.</p>
      <p><b>Hersteller:</b> Wir arbeiten mit qualitativ hochwertigen Anlagen von Namhaften Herstellern wie z.B. Voltano, Kerbosol, Solvani, Lumatec</p>
    </div>
  </div>
  <div class="page charge">
    <h2>Ladeinfrastruktur<br>und Elektromobilität</h2>
    <p class="intro">Egal ob Wallbox mit Überschussladen, oder mehrere mit intelligentem Lastmanagement, Ladepark oder Tiefgarage, gerne beraten wir Sie auch hierzu.</p>
    <div class="photo" role="img" aria-label="Schwarze Wallbox mit Ladekabel" style="left:80px;top:176px;width:52px;height:220px;background:linear-gradient(180deg,#222,#111)"></div>
    <div class="photo" role="img" aria-label="Schwarze Ladesäule mit Kabel" style="left:216px;top:176px;width:52px;height:220px;background:linear-gradient(180deg,#2a2a2a,#0f0f0f)"></div>
    <div class="photo" role="img" aria-label="Weiß-graue Ladesäule mit Kabel" style="left:366px;top:170px;width:80px;height:225px;background:linear-gradient(180deg,#fafafa 0%,#eee 40%,#4c5653 42%,#3c4442)"></div>
    <div class="quote" role="img" aria-label="Wallbox an Betonwand in einer Garage"></div>
    <svg class="qmark" width="60" height="36" viewBox="0 0 60 36"><path d="M3 3h22v10L12 33M33 3h22v10L42 33" fill="none" stroke="#fff" stroke-width="3"/></svg>
    <div class="quote-text">Mit AMPERO V2H bietet der Stromspeicher-Spezialist VOLTANO ab sofort eine bidirektionale Ladeoption für das Hauskraftwerk.</div>
    <div class="qline"></div>
  </div>
</section>

<section class="spread s4">
  <div class="page maint">
    <div class="head">
      <h2>Wartung-Service-Monitoring</h2>
      <div class="rule"></div>
    </div>
    <p>Gerade die Themen Instandhaltung, Pflege und Überwachung spielen für einen maximalen Ertrag eine wichtige Rolle. Für einen sorgenfreien Betrieb Ihrer Anlage, stehen wir Ihnen natürlich auch nach der Inbetriebnahme mit unserem Fachwissen gerne zur Seite.</p>
    <div class="photo" role="img" aria-label="Techniker prüft Solarmodule auf einem Dach" style="left:23px;top:296px;width:470px;height:434px;background:linear-gradient(180deg,#9aa0a5,#3d5d92 40%,#8fa4bf 60%,#2f4a78)"></div>
  </div>
  <div class="page back">
    <div class="band-top"></div>
    <div class="brand"><span class="mark"></span>NORDWERK ENERGIE</div>
    <p>Starten Sie jetzt Ihre ganz persönliche Energiewende und vereinbaren Sie noch heute einen kostenfreien <b>Beratungstermin</b> unter <b>08100 – 5550100.</b></p>
    <div class="band-bot"></div>
  </div>
</section>

</body>
</html>
```